電子書籍の表紙を作成お願い致します。

50歳以上の更年期女性が対象のダイエット本です。
更年期をむかえてから、ソウルメロディダイエットで7キロ痩せることに成功した体験が書かれています。

たくさんあるダイエット本に埋もれないような、
ダイエットという言葉に反応する、美意識の高い更年期女性の目につく、明るく楽し気なデザインを期待しています。

その他、何か不明な点等ございましたら、お気軽におtぴ合わせください。

宜しくお願い致します。

著者顔写真と原稿を追記します。
参考にしてください。
著者の肩書は、
ダイエットアドバイザー フィットネスインストラクター
とよろしくお願いいたします。
募集締め切りがいよいよ16時間をきりました。
すでに、いくつかの素敵なデザインをいただいていますが、
最後の逆転大ホームランを狙っている、あなたの応募を心よりお待ちしています。

選んだ理由としては、
①美意識高い女性が好むピンクがメインのデザイン
②ソウルメロディダイエットもタイトルが一番見やすい
③ビフォーアフターのイラストが可愛い
などです。

この度は、たくさんの素敵なデザインを提案いただき、本当にありがとうございました。
初めての電子書籍で大変でしたが、デザイナーの皆さんのおかげで、毎日ワクワクして、
この表紙選定が一番楽しい作業になりました。

今回残念ながら、次点になった2点もとても評判が良いものでした。
そのほかのデザインも、とても個性的で素敵でした。
本当にありがとうございました。

次回お世話になる際には、またよろしくお願いいたします。

```html
<!DOCTYPE html>
<html lang="ja">
<head>
<meta charset="utf-8">
<title>50歳からのソウルメロディダイエット</title>
<link rel="stylesheet" href="https://fonts.googleapis.com/css2?family=Noto+Sans+JP:wght@500;700;900&family=Zen+Maru+Gothic:wght@500;700;900&display=swap">
<style>
:root{
  --pink:#e8477a;
  --pink-deep:#d62f6a;
  --pink-soft:#f7b9c8;
  --pink-pale:#fde6ec;
  --ink:#1d1d1d;
  --white:#ffffff;
}
*{margin:0;padding:0;box-sizing:border-box}
html,body{width:749px;height:1200px;overflow:hidden;background:var(--white)}
.cover{position:relative;width:749px;height:1200px;overflow:hidden;background:var(--white);font-family:"Noto Sans JP",sans-serif;color:var(--ink)}
.cover p,.cover span{white-space:nowrap}
.hero-photo{position:absolute;left:270px;top:0;width:479px;height:540px;background:radial-gradient(ellipse at 50% 38%,#f3dccf 0%,#e9c8b6 35%,#f6ece6 70%,#ffffff 100%)}
.waist-photo{position:absolute;left:545px;top:410px;width:204px;height:480px;background:linear-gradient(180deg,#f4ded3 0%,#f0d4c6 45%,#c9d4e6 70%,#8ea3c8 100%);border-radius:70px 0 0 40px}
.subtitle{position:absolute;left:140px;top:22px;writing-mode:vertical-rl;font-family:"Zen Maru Gothic",sans-serif;font-weight:900;font-size:36px;line-height:1.3;transform:rotate(-5deg);transform-origin:top right}
.kicker{position:absolute;left:655px;top:8px;writing-mode:vertical-rl;font-family:"Zen Maru Gothic",sans-serif;font-weight:900;font-size:58px;color:var(--pink);letter-spacing:2px;transform:rotate(-6deg)}
.headline{position:absolute;left:505px;top:155px;writing-mode:vertical-rl;font-weight:900;font-size:118px;line-height:1;color:var(--pink);transform:rotate(-6deg);text-shadow:0 0 6px var(--white),0 0 2px var(--white)}
.age{position:absolute;left:100px;top:470px;font-weight:900;font-size:48px;line-height:1.4;z-index:2}
.age .num{font-size:84px}
.title-band{position:absolute;left:70px;top:590px;width:560px;height:82px;background:linear-gradient(90deg,rgba(247,185,200,0) 0%,var(--pink-soft) 12%,var(--pink-pale) 88%,rgba(253,230,236,0) 100%);border-radius:40px 8px 40px 8px;z-index:1}
.title-top{position:absolute;left:90px;top:578px;font-weight:900;font-size:78px;line-height:1.3;color:var(--pink-deep);letter-spacing:1px;z-index:2;text-shadow:0 0 4px var(--white)}
.title-main{position:absolute;left:70px;top:680px;font-weight:900;font-size:118px;line-height:1.3;letter-spacing:-4px;z-index:2;text-shadow:0 0 4px var(--white)}
.footer-band{position:absolute;left:0;top:888px;width:749px;height:312px;background:linear-gradient(180deg,#fbd5dc 0%,var(--pink-soft) 100%)}
.author-photo{position:absolute;left:25px;top:912px;width:190px;height:220px;border-radius:50%;background:radial-gradient(circle at 50% 40%,#f2d6c8 0%,#d8a99b 55%,#b98a84 100%);border:5px solid var(--white)}
.offer{position:absolute;left:262px;top:920px;width:375px;text-align:center}
.offer-lead{color:var(--pink);font-family:"Zen Maru Gothic",sans-serif;font-weight:700;font-size:18px;line-height:1.4}
.offer-title{margin:8px auto 0;width:375px;background:var(--white);border:3px solid var(--pink);color:var(--pink-deep);font-weight:900;font-size:32px;line-height:1.55;border-radius:6px}
.offer-detail{margin-top:6px;font-family:"Zen Maru Gothic",sans-serif;font-weight:700;font-size:16px;line-height:1.4;color:var(--ink)}
.offer-detail strong{font-size:24px;color:var(--pink-deep)}
.author-role{position:absolute;left:237px;top:1118px;font-size:14px;font-weight:700;line-height:1.4}
.author-name{position:absolute;left:465px;top:1104px;font-family:"Zen Maru Gothic",sans-serif;font-weight:900;font-size:44px;line-height:1.3}
</style>
</head>
<body>
<main class="cover">
  <div class="hero-photo" role="img" aria-label="頬に手を添えて微笑む女性の写真"></div>
  <div class="waist-photo" role="img" aria-label="引き締まったウエストの女性の写真"></div>
  <p class="subtitle">更年期でも<br>７キロ痩せられた！</p>
  <p class="kicker">これが</p>
  <h2 class="headline">最後！</h2>

  <p class="age"><span class="num">50</span>歳からの</p>
  <div class="title-band"></div>
  <h1>
    <span class="title-top">ソウルメロディ</span>
    <span class="title-main">ダイエット</span>
  </h1>

  <section class="footer-band"></section>
  <div class="author-photo" role="img" aria-label="著者の顔写真"></div>
  <div class="offer">
    <p class="offer-lead">トークアプリに登録くださった方に</p>
    <p class="offer-title">読者限定プレゼント</p>
    <p class="offer-detail">家事の合間の3分で出来る<br><strong>おなか引き締め動画</strong></p>
  </div>
  <p class="author-role">ダイエットアドバイザー<br>フィットネスインストラクター</p>
  <p class="author-name">森川ゆりこ</p>
</main>
</body>
</html>
```